School Hallway Magnetic Display Design for school values

I am looking for a someone to help me design a magnetic hallway display that will hang in the hallway of our small school. There are several elements, including 1. 6ft by 4ft designed magnetic bulletin board, 2. Magnets that will stick to the board. See attachment for which elements belong where. The display will be for our TAVRON program, which rewards students for demonstrating our school values. We want the display to be beautiful and interactive. We are also rebranding, so we want the design to align with our new fonts and colors. In the attached PDF is an outline of our new brand guidelines. Unfortunately, we don't have the color codes, but I'm hoping that you can match the colors listed. Attached are elements to be used on the board, but please use your creativity to make it more dynamic and visually appealing. For example, the star magnets could be another shape. The TAVRON magnets must remain the same. I've included two photos of boards at other schools that inspired this project.

Target Market(s)

School Community

Industry/Entity Type

Education

Requirements
Should not have
• School Logo

```html
<!DOCTYPE html>
<html lang="en">
<head>
<meta charset="utf-8">
<title>TAVRON of The Month – Hallway Board</title>
<link href="https://fonts.googleapis.com/css2?family=Montserrat:wght@600;700;800&family=Patrick+Hand&display=swap" rel="stylesheet">
<style>
  :root {
    --navy: #2e5b92;
    --sky: #b3cfe5;
    --sage: #d5dfbc;
    --sun: #fbdc82;
    --cream: #f7f7ef;
    --frame: #cfcfcf;
    --page: #f7f7f7;
    --white: #ffffff;
  }
  * { box-sizing: border-box; margin: 0; padding: 0; }
  html, body {
    width: 1200px; height: 1137px; overflow: hidden;
    background: var(--page);
  }
  .board {
    position: absolute; left: 71px; top: 214px;
    width: 1072px; height: 716px;
    background: var(--cream);
    box-shadow: 0 2px 6px rgba(0,0,0,0.18);
    overflow: hidden;
  }
  .tile { position: absolute; }
  .top-corner { left: 0; top: 0; width: 134px; height: 68px; background: linear-gradient(to top right, var(--navy) 50%, var(--sun) 50%); }
  .top-sky { left: 134px; top: 0; width: 270px; height: 68px; background: var(--sky); }
  .top-sage { left: 404px; top: 0; width: 133px; height: 68px; background: var(--sage); }
  .top-sun { left: 537px; top: 0; width: 180px; height: 68px; background: var(--sun); }

  .title-panel {
    position: absolute; left: 0; top: 68px; width: 717px; height: 287px;
    background: var(--frame); padding: 5px;
  }
  .title-card {
    position: relative; width: 100%; height: 100%;
    background: var(--white);
  }
  .title {
    position: absolute; left: 19px; top: 22px;
    font-family: "Montserrat", sans-serif; font-weight: 700;
    font-size: 57px; line-height: 1; color: var(--navy); letter-spacing: 0.5px;
  }
  .subtitle {
    position: absolute; left: 19px; top: 80px;
    font-family: "Patrick Hand", cursive; font-size: 33px;
    color: var(--navy); letter-spacing: 1px;
  }
  .thermometer { position: absolute; left: 578px; top: 32px; width: 92px; height: 216px; }

  .art-column { left: 5px; top: 355px; width: 129px; height: 361px;
    background: linear-gradient(to bottom, var(--sun) 0 33%, var(--sky) 33% 82%, var(--cream) 82%); }
  .art-scene { left: 134px; top: 355px; width: 270px; height: 361px;
    background: linear-gradient(to bottom, var(--cream) 0 55%, var(--sage) 55% 85%, var(--navy) 85%); }
  .art-grid { left: 404px; top: 355px; width: 313px; height: 361px;
    background: linear-gradient(135deg, var(--sky), var(--sun) 50%, var(--sage)); }

  .values {
    position: absolute; left: 717px; top: 0; width: 355px; height: 716px;
    background: var(--navy);
    list-style: none; padding: 70px 0 0 26px;
  }
  .value {
    display: flex; align-items: center;
    width: 312px; height: 84px; margin-bottom: 15.5px;
    border-radius: 42px; padding-left: 8px;
    font-family: "Montserrat", sans-serif; font-weight: 600;
    font-size: 29px; color: var(--navy);
  }
  .value--sage { background: var(--sage); }
  .value--sky { background: var(--sky); }
  .value--sun { background: var(--sun); }
  .value-initial {
    display: flex; align-items: center; justify-content: center;
    width: 68px; height: 68px; border-radius: 50%;
    background: var(--cream); margin-right: 8px;
    font-weight: 800; font-size: 38px;
  }
</style>
</head>
<body>
  <main class="board">
    <div class="tile top-corner"></div>
    <div class="tile top-sky" role="img" aria-label="Flat cloud shape on a sky blue tile"></div>
    <div class="tile top-sage"></div>
    <div class="tile top-sun" role="img" aria-label="Flat cloud shape on a yellow tile"></div>

    <section class="title-panel">
      <div class="title-card">
        <h1 class="title">TAVRON</h1>
        <p class="subtitle">of The Month</p>
        <svg class="thermometer" viewBox="0 0 92 216" aria-hidden="true">
          <path d="M18 20 a14 14 0 0 1 28 0 V150 a28 28 0 1 1 -28 0 Z" fill="none" stroke="#2e5b92" stroke-width="6"/>
          <rect x="29" y="85" width="6" height="80" fill="#b3cfe5"/>
          <circle cx="32" cy="176" r="17" fill="#b3cfe5"/>
          <g stroke="#2e5b92" stroke-width="5">
            <line x1="62" y1="32" x2="86" y2="32"/>
            <line x1="62" y1="68" x2="86" y2="68"/>
            <line x1="62" y1="104" x2="86" y2="104"/>
            <line x1="62" y1="140" x2="86" y2="140"/>
          </g>
        </svg>
      </div>
    </section>

    <div class="tile art-column" role="img" aria-label="Geometric butterfly and leaf tiles"></div>
    <div class="tile art-scene" role="img" aria-label="Geometric landscape with two trees, a cloud and hills"></div>
    <div class="tile art-grid" role="img" aria-label="Grid of geometric heart and flower tiles"></div>

    <ul class="values">
      <li class="value value--sage"><span class="value-initial">S</span>implicity</li>
      <li class="value value--sky"><span class="value-initial">P</span>eace</li>
      <li class="value value--sun"><span class="value-initial">I</span>ntegrity</li>
      <li class="value value--sage"><span class="value-initial">C</span>ommunity</li>
      <li class="value value--sky"><span class="value-initial">E</span>quality</li>
      <li class="value value--sun"><span class="value-initial">S</span>tewardship</li>
    </ul>
  </main>
</body>
</html>
```